New Web Page Design - Cement Rendering Business

Looking for a overhaul of our existing website (www.norpex.com.au).

Looking for a sleek and elegant design that incorporates the colours of our logos, black / green and white. Needs to look professional and want it to be well above what our competition is offering. (Findora search for 'cement rendering sydney' will display the competition we want to be well ahead of.

Prefer a mixture of pages with black background and white alternatively between home (black), about us (white), contact us (black) and gallery (white).

Would like to incorporate our logo on all pages attached preferably in the top left corner.

Website needs to be search engine optimised and have easily updated photo gallery which we already have.

Also need to embed our trackwise metrics code on the front home page.

Website needs to be able easily updated (text, pictures ) as required.
content management system should include fields where you can alter your page titles, meta description and keywords.

Pages also needs to be optimised for mobile devices, iphone, ipad and other mobile devices. (it is a current feature we have)

If you have any questions, just message me.

Please remember the look and feel of the site is important to us, we don't want it over complicated, simple elegant and professional in line with our logo standards.
Updates

Hi All, As an example of the look and feel we like. We have found a site that may assist in your design and creative process. http://demo.quorvix.org/ We like the simplicity, elegance and professional look of this site, although we would like it with our images, colours and logos. I hope this helps.! keep the great designs coming!

All, Thanks for the designs. Please try and use our website images due to copyright reasons for all your designs. Tomas

Target Market(s)

Construction Companies

Industry/Entity Type

Business

Colors
9bcb3b
acd036
474747

Requirements
Must have
• Search Engine Optimised.
Photo Gallery
Elegant/Professional Look & Feel.
Simple Yet Effective
Nice to have
• Moving Parts
Should not have
• Overly Complicated.
Cheap & Traditional Looking.
Boring

```html
<!DOCTYPE html>
<html lang="en">
<head>
<meta charset="utf-8">
<title>Norpex Cement Rendering</title>
<link rel="stylesheet" href="https://fonts.googleapis.com/css2?family=Montserrat:wght@600&family=Open+Sans:wght@400&family=Raleway:wght@400&family=Roboto:wght@300;400;500&display=swap">
<style>
:root{
  --black:#000;
  --green:#8dbf3f;
  --green-text:#6a9a12;
  --white:#fff;
  --body-grey:#6b6b6b;
  --footer-bg:#474747;
  --footer-base:#3c3c3c;
  --footer-text:#c9c9c9;
  --footer-head:#f2f2f2;
  --footer-brand:#a8a8a8;
}
*{box-sizing:border-box;margin:0;padding:0}
html,body{width:1023px;height:1200px;overflow:hidden;background:var(--white)}
body{position:relative;font-family:"Open Sans",Arial,sans-serif;color:var(--body-grey)}
a{color:inherit;text-decoration:none}

/* Hero */
.hero{position:absolute;left:0;top:0;width:1023px;height:442px;background:var(--black);overflow:hidden}
.hero-photo{position:absolute;left:380px;top:50px;width:643px;height:392px;
  background:radial-gradient(ellipse at 70% 45%,#5a5b5b 0%,#3e3f3f 45%,#1a1a1a 75%,#000 100%)}
.hero-photo::after{content:"";position:absolute;inset:0;
  background:linear-gradient(90deg,#000 0%,rgba(0,0,0,0) 35%),linear-gradient(180deg,#000 0%,rgba(0,0,0,0) 20%)}
.brand-name{position:absolute;left:103px;top:28px;font-family:"Open Sans",sans-serif;font-weight:400;font-size:34px;line-height:40px;color:var(--white)}
.main-nav{position:absolute;right:102px;top:34px;width:321px;border-bottom:1px solid #4a4a4a;display:flex;justify-content:space-between;height:27px}
.main-nav a{font-size:11px;color:var(--white);text-transform:uppercase;line-height:18px;position:relative}
.main-nav a.active::after{content:"";position:absolute;left:0;right:0;top:25px;height:2px;background:var(--green)}
.hero-title{position:absolute;left:103px;top:155px;font-family:"Montserrat",sans-serif;font-weight:600;font-size:26.5px;line-height:32px;color:var(--white)}
.hero-text{position:absolute;left:104px;top:234px;width:335px;font-size:10.6px;line-height:17px;color:var(--white)}
.btn{position:absolute;left:102px;top:322px;width:114px;height:24px;background:var(--green);color:#2e3d10;font-size:11px;line-height:24px;text-align:center}

/* About + News */
.section-title{font-family:"Open Sans",sans-serif;font-weight:400;font-size:20px;color:#111}
.about{position:absolute;left:102px;top:483px;width:545px}
.about p{font-size:10.6px;line-height:17px;margin-top:14px}
.about p + p{margin-top:17px}
.news{position:absolute;left:693px;top:483px;width:230px}
.news-dots{position:absolute;right:2px;top:14px;display:flex;gap:8px}
.news-dots span{width:6px;height:6px;border-radius:50%;background:#888}
.news-dots span.on{background:#000}
.news-item{margin-top:14px}
.news-item h3{font-weight:400;font-size:9.5px;line-height:13px;color:var(--green-text);padding-left:2px;width:185px}
.news-item p{font-size:9.5px;line-height:13px;margin-top:7px}

/* Service cards */
.card{position:absolute;top:708px;width:252px}
.card-photo{height:113px;border-radius:3px}
.card h2{font-family:"Raleway",sans-serif;font-weight:400;font-size:16.5px;color:#111;margin-top:11px}
.card p{font-size:9.5px;line-height:13.6px;margin-top:5px;width:236px}
.card .more{display:inline-block;margin-top:6px;font-size:9.5px;font-style:italic;color:var(--green-text)}
.card .more svg{vertical-align:middle;margin-left:6px}

/* Footer */
.footer{position:absolute;left:0;top:986px;width:1023px;height:171px;background:var(--footer-bg);font-family:"Roboto",Arial,sans-serif}
.footer-col{position:absolute;top:33px}
.footer-col h4{font-weight:500;font-size:12px;color:var(--footer-head);text-transform:uppercase}
.footer-col ul{list-style:none;margin-top:14px}
.footer-col li{font-size:10.5px;color:var(--footer-text);line-height:20.5px;padding-left:9px;position:relative;font-weight:300}
.footer-col li::before{content:"";position:absolute;left:0;top:6px;border-left:3px solid var(--footer-text);border-top:3px solid transparent;border-bottom:3px solid transparent}
.contact-row{display:flex;gap:10px;color:var(--footer-text);font-size:10.5px;font-weight:300;margin-top:10px;line-height:14px}
.contact-row svg{flex:none}
.contact-row.phone{font-size:14px;font-weight:400}
.footer-brand{position:absolute;right:102px;top:40px;font-family:"Open Sans",sans-serif;font-weight:400;font-size:34px;line-height:40px;color:var(--footer-brand)}
.follow{position:absolute;right:102px;top:128px;display:flex;align-items:center;gap:5px;font-size:10.5px;color:var(--footer-text)}
.follow span.social{width:22px;height:22px;border:1.5px solid #bdbdbd;border-radius:50%}
.follow .label{margin-right:3px}
.base{position:absolute;left:0;top:1157px;width:1023px;height:43px;background:var(--footer-base);font-size:10.5px;color:#bbb}
.base .copy{position:absolute;left:102px;top:15px}
.base .legal{position:absolute;right:109px;top:15px;font-family:"Roboto",sans-serif}
.base .legal a{text-decoration:underline}
</style>
</head>
<body>

<header class="hero">
  <div class="hero-photo" role="img" aria-label="Gloved hand spreading cement render on a wall with a trowel"></div>
  <div class="brand-name">Norpex</div>
  <nav class="main-nav">
    <a href="#" class="active">Home</a>
    <a href="#">About Us</a>
    <a href="#">Photo Gallery</a>
    <a href="#">Contact Us</a>
  </nav>
  <h1 class="hero-title">Welcome To The<br>Norpex Cement Rendering</h1>
  <p class="hero-text">Sed ut perspiciatis unde omnis iste natus error sit voluptatem accusantium doloremque laudantium, totam rem aperiam, eaque ipsa quae ab illo inventore veritatis et quasi architecto beatae vitae dicta sunt explicabo.</p>
  <a class="btn" href="#">Read More</a>
</header>

<section class="about">
  <h2 class="section-title">About Norpex Cement Rendering</h2>
  <p>Your one stop shop for all your cement rendering needs. We are an Australian owned and operated business with over 25 years of experience in our field, Our work is fully licensed, our employee's are trained to the highest standards and all of our work is covered by warranty.</p>
  <p>We offer an obligation free on-site consultation and quotation service for your convenience 7 days per week We are the preferred supplier for many of the top building companies in Australia which gives you the access to our expertise, competetive rates and peace of mind No job is too big or too small. We work on several residential, private and commercial projects all year round.</p>
</section>

<aside class="news">
  <h2 class="section-title">Latest New’s</h2>
  <div class="news-dots"><span></span><span></span><span class="on"></span></div>
  <div class="news-item">
    <h3>Lorem ipsum dolor sitamet, consectetur adipiscing elit.</h3>
    <p>Lorem ipsum dolor sit amet, consectetur adipiscing elit. Donec hendrerit vehicula est, in consequat</p>
  </div>
  <div class="news-item">
    <h3>Lorem ipsum dolor sitamet, consectetur adipiscing elit.</h3>
    <p>Lorem ipsum dolor sit amet, consectetur adipiscing elit. Donec hendrerit vehicula est, in consequat</p>
  </div>
</aside>

<article class="card" style="left:102px">
  <div class="card-photo" role="img" aria-label="Worker smoothing a concrete floor with a float" style="background:linear-gradient(135deg,#8a8a86,#6f706c 60%,#b9b4ad)"></div>
  <h2>Lorem ipsum</h2>
  <p>Sed ut perspiciatis unde omnis iste natus error sit totam rem aperiam eaque ipsa quae ab illo inventore veritatis et quasi architecto beatae vitae dicta sunt explicabo.</p>
  <a class="more" href="#">Read More<svg width="14" height="6" viewBox="0 0 14 6"><path d="M0 3H13M10 0.5L13 3 10 5.5" fill="none" stroke="#6a9a12"/></svg></a>
</article>

<article class="card" style="left:386px">
  <div class="card-photo" role="img" aria-label="Hand laying red bricks with a trowel" style="background:linear-gradient(180deg,#e6e6e4 0%,#d8d6d2 40%,#b5583a 60%,#9a4a33 100%)"></div>
  <h2>Eiusmod Tempor</h2>
  <p>Sed ut perspiciatis unde omnis iste natus error sit totam rem aperiam eaque ipsa quae ab illo inventore veritatis et quasi architecto beatae vitae dicta sunt explicabo.</p>
  <a class="more" href="#">Read More<svg width="14" height="6" viewBox="0 0 14 6"><path d="M0 3H13M10 0.5L13 3 10 5.5" fill="none" stroke="#6a9a12"/></svg></a>
</article>

<article class="card" style="left:669px">
  <div class="card-photo" role="img" aria-label="Builder in a yellow hard hat checking a wall with a spirit level" style="background:linear-gradient(90deg,#a9a9a6 0%,#8c8f8e 30%,#c59a5a 65%,#7c6a4e 100%)"></div>
  <h2>&nbsp;Incididunt ut Labore</h2>
  <p>Sed ut perspiciatis unde omnis iste natus error sit totam rem aperiam eaque ipsa quae ab illo inventore veritatis et quasi architecto beatae vitae dicta sunt explicabo.</p>
  <a class="more" href="#">Read More<svg width="14" height="6" viewBox="0 0 14 6"><path d="M0 3H13M10 0.5L13 3 10 5.5" fill="none" stroke="#6a9a12"/></svg></a>
</article>

<footer class="footer">
  <div class="footer-col" style="left:103px">
    <h4>Who We Are</h4>
    <ul><li>About Us</li><li>Products</li><li>News</li><li>Gallery</li></ul>
  </div>
  <div class="footer-col" style="left:271px">
    <h4>Our Services</h4>
    <ul><li>Concrete Sleepers</li><li>Concrete Retaining Walls</li><li>Concrete Plinths</li><li>Concrete Plinths</li></ul>
  </div>
  <div class="footer-col" style="left:481px">
    <h4>Contact Us</h4>
    <div class="contact-row" style="margin-top:12px">
      <svg width="12" height="15" viewBox="0 0 12 15"><path d="M6 0a5 5 0 0 0-5 5c0 4 5 10 5 10s5-6 5-10a5 5 0 0 0-5-5z" fill="#bdbdbd"/><circle cx="6" cy="5" r="2" fill="#474747"/></svg>
      <span>Address: 1234 Street Name,<br>City, State 12354.</span>
    </div>
    <div class="contact-row phone">
      <svg width="15" height="16" viewBox="0 0 15 16"><path d="M3 1l3 3-2 2c1 2 3 4 5 5l2-2 3 3-2 3C6 15 0 9 0 4z" fill="#bdbdbd"/></svg>
      <span>1233-456-7890</span>
    </div>
    <div class="contact-row">
      <svg width="16" height="11" viewBox="0 0 16 11"><rect x="0.5" y="0.5" width="15" height="10" fill="none" stroke="#bdbdbd"/><path d="M0.5 0.5L8 6l7.5-5.5" fill="none" stroke="#bdbdbd"/></svg>
      <span>info@domainname.com</span>
    </div>
  </div>
  <div class="footer-brand">Norpex</div>
  <div class="follow" aria-label="Social profiles">
    <span class="label">Follow us:</span>
    <span class="social"></span><span class="social"></span><span class="social"></span><span class="social"></span><span class="social"></span>
  </div>
</footer>

<div class="base">
  <span class="copy">Copyright &nbsp;© 2014 norpex.all right reserved</span>
  <span class="legal"><a href="#">Terms &amp; Conditons</a> &nbsp;| &nbsp;<a href="#">Privacy Policy</a></span>
</div>

</body>
</html>
```